FARLOW'S needs a label design for a Moruga Scorpion Pepper Hot Sauce (5oz bottle)

We need a label for a new company based in south Mississippi called FARLOW'S. We have a new hot sauce made from Moruga Scorpion Peppers that's very hot yet has "layers of flavor". The sauce is a deep red color in a clear bottle. We are looking for something simple yet different and will stand out. We would like to limit the design to 3 colors.

It Company

• wide latin?

```html
<!DOCTYPE html>
<html lang="en">
<head>
<meta charset="utf-8">
<title>FARLOW'S Hot Sauce Labels</title>
<link rel="stylesheet" href="https://fonts.googleapis.com/css2?family=Arimo:wght@400;700&family=PT+Sans:wght@400;700&display=swap">
<style>
  :root {
    --label-green: #13934a;
    --label-red: #a01f23;
    --label-orange: #fbb03b;
    --text-dark: #1a1a1a;
    --text-maroon: #8e1c1f;
    --white: #ffffff;
    --page: #ffffff;
  }
  html, body {
    margin: 0;
    padding: 0;
    width: 1200px;
    height: 1000px;
    overflow: hidden;
    background: var(--page);
  }
  .canvas {
    position: relative;
    width: 1200px;
    height: 1000px;
  }
  .front-label {
    position: absolute;
    left: 330px;
    top: 568px;
    width: 226px;
    height: 234px;
  }
  .front-label svg { display: block; }
  .brand-name {
    font-family: "Arimo", Arial, sans-serif;
    font-weight: 700;
    font-size: 29px;
    fill: var(--white);
    letter-spacing: 1px;
  }
  .tagline {
    font-family: "Arimo", Arial, sans-serif;
    font-size: 15.5px;
    fill: var(--white);
    letter-spacing: 0.3px;
  }
  .product-name {
    font-family: "Arimo", Arial, sans-serif;
    font-size: 17px;
    fill: var(--text-dark);
  }
  .net-weight {
    font-family: "Arimo", Arial, sans-serif;
    font-weight: 700;
    font-size: 15px;
    fill: var(--white);
  }

  .back-label {
    position: absolute;
    left: 927px;
    top: 517px;
    width: 211px;
    height: 314px;
    box-sizing: border-box;
    background: var(--label-orange);
    border-radius: 9px;
    padding: 5px;
  }
  .back-label-frame {
    box-sizing: border-box;
    height: 100%;
    border: 1.2px solid var(--white);
    border-radius: 6px;
    padding: 20px 16px 0 17px;
    font-family: "PT Sans", Arial, sans-serif;
    font-size: 11px;
    line-height: 14.5px;
    color: var(--text-dark);
  }
  .panel-title {
    margin: 0;
    font-size: 11px;
    font-weight: 700;
    color: var(--text-maroon);
  }
  .panel-line { margin: 0; }
  .panel-line strong { font-weight: 700; }
  .nutrition-table {
    border-collapse: collapse;
    font-size: 11px;
    line-height: 14.5px;
  }
  .nutrition-table td, .nutrition-table th {
    padding: 0;
    font-weight: 400;
    white-space: nowrap;
  }
  .nutrition-table th {
    color: var(--text-maroon);
    text-align: center;
  }
  .nutrition-table .col-label { width: 53px; text-align: left; }
  .nutrition-table .col-serving { width: 60px; text-align: center; }
  .nutrition-table .col-hundred { width: 66px; text-align: right; }
  .nutrition-table .note-row td { padding-left: 10px; }
  .ingredients {
    margin: 20px 0 0;
    line-height: 14px;
  }
  .ingredients-label { color: var(--text-maroon); font-weight: 700; }
  .distributor {
    margin: 10px 0 0;
    font-weight: 700;
    color: var(--text-maroon);
  }
</style>
</head>
<body>
<main class="canvas">

  <section class="front-label" aria-label="Front label">
    <svg width="226" height="234" viewBox="0 0 226 234">
      <defs>
        <clipPath id="label-shape">
          <path d="M0,42 Q0,28 11,26 Q23,24 31,15 Q62,0 113,0 Q164,0 195,15 Q203,24 215,26 Q226,28 226,42 L226,192 Q226,206 215,208 Q203,210 195,219 Q164,234 113,234 Q62,234 31,219 Q23,210 11,208 Q0,206 0,192 Z"/>
        </clipPath>
        <path id="tagline-arc" d="M26,80 Q113,14 200,80"/>
      </defs>
      <g clip-path="url(#label-shape)">
        <rect class="band-green" x="0" y="0" width="226" height="88" fill="var(--label-green)"/>
        <rect class="band-red" x="0" y="88" width="226" height="40" fill="var(--label-red)"/>
        <rect class="band-orange" x="0" y="128" width="226" height="106" fill="var(--label-orange)"/>
      </g>
      <path class="dotted-border" d="M0,42 Q0,28 11,26 Q23,24 31,15 Q62,0 113,0 Q164,0 195,15 Q203,24 215,26 Q226,28 226,42 L226,192 Q226,206 215,208 Q203,210 195,219 Q164,234 113,234 Q62,234 31,219 Q23,210 11,208 Q0,206 0,192 Z"
            transform="translate(113 117) scale(0.955 0.955) translate(-113 -117)"
            fill="none" stroke="var(--white)" stroke-width="1.3" stroke-dasharray="0.1 3" stroke-linecap="round"/>
      <text class="tagline"><textPath href="#tagline-arc" startOffset="50%" text-anchor="middle">LAYERS OF FLAVOR</textPath></text>
      <text class="brand-name" x="113" y="119" text-anchor="middle">FARLOW'S</text>
      <rect class="pepper-art" x="72" y="130" width="76" height="40" rx="16" fill="var(--label-red)" role="img" aria-label="Illustration of two red Moruga Scorpion peppers"/>
      <text class="product-name" x="113" y="194" text-anchor="middle">HOT SAUCE</text>
      <text class="net-weight" x="113" y="218" text-anchor="middle">5oz</text>
    </svg>
  </section>

  <section class="back-label" aria-label="Back label">
    <div class="back-label-frame">
      <h2 class="panel-title">Nutrition Information</h2>
      <p class="panel-line"><strong>Serving per package:</strong> 85</p>
      <p class="panel-line"><strong>Serving size:</strong> 1g or 1/4 tsp</p>
      <table class="nutrition-table">
        <tr><td class="col-label"></td><th class="col-serving">Per Serving</th><th class="col-hundred">Per 100 g</th></tr>
        <tr><td class="col-label">Energy</td><td class="col-serving">10kJ</td><td class="col-hundred">1000 kJ</td></tr>
        <tr><td class="col-label">Protein</td><td class="col-serving">0.1g</td><td class="col-hundred">10.4 g</td></tr>
        <tr class="note-row"><td colspan="3">*Gluten Not detected...................</td></tr>
        <tr><td class="col-label">Fat, total</td><td class="col-serving">0.1g</td><td class="col-hundred">10.0 g</td></tr>
        <tr><td class="col-label">*Saturated</td><td class="col-serving">0.0g</td><td class="col-hundred">0.9 g</td></tr>
        <tr><td class="col-label">Carbohydrate</td><td class="col-serving">0.4g</td><td class="col-hundred">36.2 g</td></tr>
        <tr><td class="col-label">*Sugar</td><td class="col-serving">0.0g</td><td class="col-hundred">3.4 g</td></tr>
        <tr><td class="col-label">Sodium</td><td class="col-serving">111mg</td><td class="col-hundred">11100mg</td></tr>
      </table>
      <p class="ingredients"><span class="ingredients-label">Ingredients:</span>Lorem ipsum dolor sit amet, mauris tristique</p>
      <p class="distributor">DIST &amp; SOLD BY FARLOW'S, MS</p>
    </div>
  </section>

</main>
</body>
</html>
```